MARLOW CREST WINE LABEL DESIGN PROJECT

We need an elegant wine label design for our new range of wine. We need 3 labels for the range

2015 MARLOW CREST SHIRAZ
2015 MARLOW CREST CABERNET SAUVIGNON
2015 MARLOW CREST CABERNET SHIRAZ

The Size is nominated at 120mm High x 90mm Wide (Front and Back) but we are open to creative expression even if size differs

We are open to any style of label and designer can work on their strengths. it can be modern/classic/old fashion etc

I have attached the marlow crest logo ( the 2 olives) and a set up called wine mandatories which is in no way a design direction just the mandatory info that needs to appear on labels. The wine mandatories is just the information that needs to go on the label it has nothing to do with the design. DO not make designs based on this at all. These labels are for red wine not olive oil.

I have also attached some of the companies current olive oil labels ( TORQUALE AND WANDELLA AND MARLOW CREST so you can see other labels and how this wine product will sit in gift baskets.

Thanks
Tomasz.

Reason: Hello Friends We have decided to extend the deadline to enable more submissions. Many of the designs submitted have images of olives and look like olive oil product. We only need the olive logo to be shown on the label but the rest of the design should be a classic simple red wine label. It is not olive oil or olive product - it is red wine. Please keep simple and stylish Thanks Tomasz

Target Market(s)

35-65

Font styles to use
Serif

Requirements
Must have
• AS per brief
Nice to have
• as per brief
Should not have
• as per brief

```html
<!DOCTYPE html>
<html lang="en">
<head>
<meta charset="utf-8">
<title>Marlow Crest Wine Labels</title>
<link rel="stylesheet" href="https://fonts.googleapis.com/css2?family=Cinzel:wght@400;700&family=Montserrat:wght@400;600&display=swap">
<style>
  :root {
    --canvas: #cdcdcd;
    --label-black: #050505;
    --ring-gold: #e0a91c;
    --text-white: #ffffff;
    --wine-hi: #c5161d;
    --wine-lo: #5e0407;
  }
  html, body {
    margin: 0;
    width: 1200px;
    height: 1200px;
    overflow: hidden;
    background: var(--canvas);
  }
  .range {
    position: relative;
    width: 1200px;
    height: 1200px;
    display: flex;
    justify-content: center;
    align-items: center;
    gap: 45px;
  }
  .label {
    width: 340px;
    height: 460px;
    display: block;
    box-shadow: 0 14px 28px rgba(0,0,0,0.25);
  }
  .label--cabernet { --panel-hi: #ffd23a; --panel-lo: #e08f00; --frame: #b87a00; --emblem: #b3141a; --panel-text: #5a0d0d; }
  .label--shiraz   { --panel-hi: #d81f26; --panel-lo: #7a0a0e; --frame: #e0a91c; --emblem: #ffffff; --panel-text: #ffffff; }
  .label--blend    { --panel-hi: #2ea24c; --panel-lo: #0d5522; --frame: #e0a91c; --emblem: #c0141b; --panel-text: #ffffff; }

  .stop-hi { stop-color: var(--panel-hi); }
  .stop-lo { stop-color: var(--panel-lo); }
  .stop-wine-hi { stop-color: var(--wine-hi); }
  .stop-wine-lo { stop-color: var(--wine-lo); }

  .label__ground { fill: var(--label-black); }
  .label__panel { stroke: var(--frame); stroke-width: 2; }
  .label__frame-line { fill: none; stroke: var(--frame); stroke-width: 1.5; }
  .label__emblem { fill: var(--emblem); }
  .label__seal-ring { fill: none; stroke: var(--ring-gold); stroke-width: 3; }
  .label__seal-inner { fill: none; stroke: var(--ring-gold); stroke-width: 0.8; }
  .label__word {
    font-family: "Montserrat", sans-serif;
    font-weight: 400;
    font-size: 44px;
    fill: var(--text-white);
  }
  .label__micro {
    font-family: "Cinzel", serif;
    font-weight: 700;
    font-size: 6px;
    letter-spacing: 1.5px;
    fill: var(--text-white);
  }
  .label__variety {
    font-family: "Cinzel", serif;
    font-weight: 700;
    font-size: 8px;
    fill: var(--panel-text);
  }
  .label__brand {
    font-family: "Cinzel", serif;
    font-weight: 700;
    font-size: 9px;
    letter-spacing: 2px;
    fill: var(--panel-text);
  }
  .label__brand-dot { fill: var(--panel-text); }
  .label__volume {
    font-family: "Montserrat", sans-serif;
    font-weight: 600;
    font-size: 11px;
    fill: var(--text-white);
  }
  .label__splash { opacity: 0.85; }
</style>
</head>
<body>
<main class="range">

  <!-- Cabernet Sauvignon -->
  <svg class="label label--cabernet" viewBox="0 0 340 460" aria-label="Marlow Crest Cabernet Sauvignon label">
    <defs>
      <linearGradient id="panel-cab" x1="0" y1="0" x2="1" y2="0">
        <stop offset="0" class="stop-lo"/><stop offset="0.45" class="stop-hi"/><stop offset="1" class="stop-lo"/>
      </linearGradient>
      <linearGradient id="splash-cab" x1="0" y1="0" x2="0" y2="1">
        <stop offset="0" class="stop-wine-hi"/><stop offset="1" class="stop-wine-lo"/>
      </linearGradient>
      <path id="arc-cab" d="M85,230 A65,65 0 0 0 215,230"/>
    </defs>
    <rect class="label__ground" width="340" height="460"/>
    <path class="label__panel" fill="url(#panel-cab)" d="M62,40 H238 Q246,58 262,62 V150 H38 V62 Q54,58 62,40 Z"/>
    <path class="label__panel" fill="url(#panel-cab)" d="M38,310 H262 V398 Q246,402 238,420 H62 Q54,402 38,398 Z"/>
    <path class="label__frame-line" d="M44,150 V310 M256,150 V310"/>
    <rect class="label__emblem" role="img" aria-label="Bull head emblem framed by laurel sprigs" x="110" y="62" width="80" height="44" rx="10"/>
    <rect class="label__splash" role="img" aria-label="Red wine pouring into a wine glass" x="238" y="30" width="82" height="390" rx="36" fill="url(#splash-cab)"/>
    <circle class="label__seal-ring" cx="150" cy="230" r="78"/>
    <circle class="label__seal-inner" cx="150" cy="230" r="70"/>
    <text class="label__micro" x="150" y="190" text-anchor="middle">WINE OF</text>
    <text class="label__micro" x="150" y="204" text-anchor="middle">BRAND</text>
    <text class="label__word" x="150" y="246" text-anchor="middle">WINE</text>
    <text class="label__micro" x="150" y="262" text-anchor="middle">ORIGIN</text>
    <text class="label__micro"><textPath href="#arc-cab" startOffset="50%" text-anchor="middle">SOUTH AUSTRALIA</textPath></text>
    <text class="label__volume" x="44" y="302">750ml</text>
    <text class="label__variety" x="150" y="330" text-anchor="middle">MARLOW CREST CABERNET SAUVIGNON</text>
    <circle class="label__brand-dot" cx="150" cy="356" r="10"/>
    <text class="label__brand" x="150" y="390" text-anchor="middle">THE MARLOW CREST.</text>
  </svg>

  <!-- Shiraz -->
  <svg class="label label--shiraz" viewBox="0 0 340 460" aria-label="Marlow Crest Shiraz label">
    <defs>
      <linearGradient id="panel-shz" x1="0" y1="0" x2="1" y2="0">
        <stop offset="0" class="stop-lo"/><stop offset="0.45" class="stop-hi"/><stop offset="1" class="stop-lo"/>
      </linearGradient>
      <linearGradient id="splash-shz" x1="0" y1="0" x2="0" y2="1">
        <stop offset="0" class="stop-wine-hi"/><stop offset="1" class="stop-wine-lo"/>
      </linearGradient>
      <path id="arc-shz" d="M85,230 A65,65 0 0 0 215,230"/>
    </defs>
    <rect class="label__ground" width="340" height="460"/>
    <path class="label__panel" fill="url(#panel-shz)" d="M62,40 H238 Q246,58 262,62 V150 H38 V62 Q54,58 62,40 Z"/>
    <path class="label__panel" fill="url(#panel-shz)" d="M38,310 H262 V398 Q246,402 238,420 H62 Q54,402 38,398 Z"/>
    <path class="label__frame-line" d="M44,150 V310 M256,150 V310"/>
    <rect class="label__emblem" role="img" aria-label="Bull head emblem framed by laurel sprigs" x="110" y="62" width="80" height="44" rx="10"/>
    <rect class="label__splash" role="img" aria-label="Red wine pouring into a wine glass" x="238" y="30" width="82" height="390" rx="36" fill="url(#splash-shz)"/>
    <circle class="label__seal-ring" cx="150" cy="230" r="78"/>
    <circle class="label__seal-inner" cx="150" cy="230" r="70"/>
    <text class="label__micro" x="150" y="190" text-anchor="middle">WINE OF</text>
    <text class="label__micro" x="150" y="204" text-anchor="middle">BRAND</text>
    <text class="label__word" x="150" y="246" text-anchor="middle">WINE</text>
    <text class="label__micro" x="150" y="262" text-anchor="middle">ORIGIN</text>
    <text class="label__micro"><textPath href="#arc-shz" startOffset="50%" text-anchor="middle">SOUTH AUSTRALIA</textPath></text>
    <text class="label__variety" x="150" y="330" text-anchor="middle">MARLOW CREST SHIRAZ</text>
    <text class="label__volume" x="52" y="362">750ml</text>
    <circle class="label__brand-dot" cx="150" cy="356" r="10"/>
    <text class="label__brand" x="150" y="390" text-anchor="middle">THE MARLOW CREST.</text>
  </svg>

  <!-- Cabernet Shiraz -->
  <svg class="label label--blend" viewBox="0 0 340 460" aria-label="Marlow Crest Shiraz label, green edition">
    <defs>
      <linearGradient id="panel-bld" x1="0" y1="0" x2="1" y2="0">
        <stop offset="0" class="stop-lo"/><stop offset="0.45" class="stop-hi"/><stop offset="1" class="stop-lo"/>
      </linearGradient>
      <linearGradient id="splash-bld" x1="0" y1="0" x2="0" y2="1">
        <stop offset="0" class="stop-wine-hi"/><stop offset="1" class="stop-wine-lo"/>
      </linearGradient>
      <path id="arc-bld" d="M85,230 A65,65 0 0 0 215,230"/>
    </defs>
    <rect class="label__ground" width="340" height="460"/>
    <path class="label__panel" fill="url(#panel-bld)" d="M62,40 H238 Q246,58 262,62 V150 H38 V62 Q54,58 62,40 Z"/>
    <path class="label__panel" fill="url(#panel-bld)" d="M38,310 H262 V398 Q246,402 238,420 H62 Q54,402 38,398 Z"/>
    <path class="label__frame-line" d="M44,150 V310 M256,150 V310"/>
    <rect class="label__emblem" role="img" aria-label="Bull head emblem framed by laurel sprigs" x="110" y="62" width="80" height="44" rx="10"/>
    <rect class="label__splash" role="img" aria-label="Red wine pouring into a wine glass" x="238" y="30" width="82" height="390" rx="36" fill="url(#splash-bld)"/>
    <circle class="label__seal-ring" cx="150" cy="230" r="78"/>
    <circle class="label__seal-inner" cx="150" cy="230" r="70"/>
    <text class="label__micro" x="150" y="190" text-anchor="middle">WINE OF</text>
    <text class="label__micro" x="150" y="204" text-anchor="middle">BRAND</text>
    <text class="label__word" x="150" y="246" text-anchor="middle">WINE</text>
    <text class="label__micro" x="150" y="262" text-anchor="middle">ORIGIN</text>
    <text class="label__micro"><textPath href="#arc-bld" startOffset="50%" text-anchor="middle">SOUTH AUSTRALIA</textPath></text>
    <text class="label__variety" x="150" y="330" text-anchor="middle">MARLOW CREST SHIRAZ</text>
    <text class="label__volume" x="52" y="362">750ml</text>
    <circle class="label__brand-dot" cx="150" cy="356" r="10"/>
    <text class="label__brand" x="150" y="390" text-anchor="middle">THE MARLOW CREST.</text>
  </svg>

</main>
</body>
</html>
```